I need a Facebook, Instagram post, for Outdoor Training
I need my logo,
Business name : Valmora Soccer Academy
Boys and girls Outdoor Soccer training
Passing, Kicking Shooting, Dribbling, Ball Control
Field: Brookvale Turf #5(1746 Hollowmere Lane Dunstead, MD 20419)
Time: 5:30pm-6:30pm 5-8 years old
6;30pm-7:30pm 9-12 years old
7:30pm-8:30pm 13-18 years old
Registration $210 ( Includes 1st month, registration, practice uniform)

Register online:
www.valmoraacademy.example
Phone:(240)555-0187

Target Market(s)

YOUTH KIDS

Colors
0054AA
0677BA
7BADD7
CADEEF
E8F1F8

Requirements
Must have
• blue , or black and white

```html
<!DOCTYPE html>
<html lang="en">
<head>
<meta charset="utf-8">
<title>Valmora Soccer Academy – Outdoor Soccer Training</title>
<link rel="stylesheet" href="https://fonts.googleapis.com/css2?family=Saira:wght@500;600;700;800&display=swap">
<style>
  :root {
    --brand-blue: #0054aa;
    --mid-blue: #0677ba;
    --column-blue: #0b5fae;
    --sky-light: #cadeef;
    --sky-top: #a9d3f3;
    --sky-pale: #e8f1f8;
    --grass: #9fbf5a;
    --grass-dark: #6f9a3c;
    --headline-gray: #4a4a4a;
    --ink: #111111;
    --yellow: #ffc400;
    --orange: #f26b12;
    --panel-light: #ececec;
    --white: #ffffff;
  }
  * { margin: 0; padding: 0; box-sizing: border-box; }
  html, body { width: 1200px; height: 1200px; overflow: hidden; background: var(--white); }
  body { font-family: "Saira", Arial, sans-serif; }
  .post { position: relative; width: 1200px; height: 1200px; overflow: hidden; }

  .hero-photo {
    position: absolute; left: 0; top: 0; width: 1200px; height: 915px;
    background: linear-gradient(180deg, var(--sky-top) 0%, var(--sky-light) 35%, var(--sky-pale) 58%, #5f8a45 72%, var(--grass) 80%, var(--grass-dark) 100%);
  }

  .headline { position: absolute; left: 0; width: 1200px; text-align: center; font-weight: 800; letter-spacing: 0.5px; }
  .headline--top { top: 72px; font-size: 60px; color: var(--brand-blue); line-height: 1; }
  .headline--main { top: 145px; font-size: 74px; color: var(--headline-gray); line-height: 1; }

  .skills-pill {
    position: absolute; left: 205px; top: 237px; width: 825px; height: 70px; border-radius: 35px;
    background: linear-gradient(180deg, var(--mid-blue), var(--brand-blue));
    color: var(--white); font-weight: 700; font-size: 29px;
    display: flex; align-items: center; justify-content: center; gap: 12px;
  }
  .skills-pill .sep { font-weight: 500; }

  .academy-badge {
    position: absolute; left: 858px; top: 732px; width: 338px; height: 338px; border-radius: 50%;
    background: var(--white); box-shadow: 0 0 0 2px var(--white) inset;
  }
  .academy-badge::after {
    content: ""; position: absolute; inset: 14px; border-radius: 50%; border: 1.5px solid var(--brand-blue);
  }
  .academy-mark {
    position: absolute; left: 146px; top: 30px; width: 46px; height: 46px; border-radius: 50%;
    background: var(--brand-blue);
  }
  .academy-name {
    position: absolute; left: 0; width: 338px; top: 92px; text-align: center;
    color: var(--brand-blue); font-weight: 800; line-height: 1.05;
  }
  .academy-name .line-1 { display: block; font-size: 38px; letter-spacing: 1px; }
  .academy-name .line-2 { display: block; font-size: 15px; letter-spacing: 4px; }

  .field-band {
    position: absolute; left: 0; top: 915px; width: 1200px; height: 62px; background: var(--ink);
    color: var(--white); font-weight: 600; font-size: 30px; display: flex; align-items: center; justify-content: center;
  }

  .info-column { position: absolute; top: 977px; height: 223px; }
  .info-column--time { left: 0; width: 471px; background: linear-gradient(180deg, #fafafa, var(--panel-light)); }
  .info-column--price { left: 471px; width: 324px; background: var(--column-blue); }
  .info-column--online { left: 795px; width: 405px; background: linear-gradient(180deg, #fafafa, var(--panel-light)); }

  .column-head {
    position: relative; height: 52px; display: flex; align-items: center; justify-content: center;
    font-weight: 800; font-size: 32px; color: var(--ink); background: var(--yellow);
  }
  .column-head::after {
    content: ""; position: absolute; left: 50%; bottom: -8px; margin-left: -8px;
    border-left: 8px solid transparent; border-right: 8px solid transparent; border-top: 8px solid var(--yellow);
  }
  .column-head--orange { background: var(--orange); color: var(--white); }
  .column-head--orange::after { border-top-color: var(--orange); }

  .schedule { list-style: none; position: absolute; left: 36px; top: 72px; }
  .schedule-row { display: flex; height: 36px; margin-bottom: 12px; font-size: 21px; font-weight: 600; color: var(--white); }
  .schedule-time {
    width: 207px; background: linear-gradient(180deg, #1a83d0, var(--brand-blue));
    border-radius: 18px 0 0 18px; display: flex; align-items: center; padding-left: 14px;
    clip-path: polygon(0 0, 94% 0, 100% 50%, 94% 100%, 0 100%);
  }
  .schedule-age {
    width: 196px; margin-left: -10px; background: linear-gradient(180deg, #3a3a3a, #000);
    border-radius: 0 18px 18px 0; display: flex; align-items: center; padding-left: 24px;
    clip-path: polygon(0 0, 100% 0, 100% 100%, 0 100%, 6% 50%);
  }

  .price { text-align: center; color: var(--white); }
  .price-amount { margin-top: 18px; font-size: 92px; font-weight: 800; line-height: 1; }
  .price-note { margin-top: 14px; font-size: 16px; font-weight: 500; line-height: 1.3; }

  .contact { text-align: center; }
  .contact-web { margin-top: 36px; font-size: 22px; font-weight: 700; color: var(--headline-gray); }
  .contact-web .domain { color: var(--brand-blue); }
  .contact-phone { margin-top: 4px; font-size: 42px; font-weight: 800; color: var(--brand-blue); letter-spacing: 0.5px; }
</style>
</head>
<body>
<main class="post">
  <div class="hero-photo" role="img" aria-label="Photo of youth players in blue and white kits dribbling balls through yellow cones on a grass field while a coach watches by a goal"></div>

  <h1 class="headline headline--top">Boys and girls</h1>
  <h2 class="headline headline--main">Outdoor Soccer training</h2>

  <div class="skills-pill">
    <span>Passing</span><span class="sep">|</span><span>Kicking Shooting</span><span class="sep">|</span><span>Dribbling</span><span class="sep">|</span><span>Ball Control</span>
  </div>

  <div class="academy-badge">
    <span class="academy-mark"></span>
    <p class="academy-name"><span class="line-1">VALMORA</span><span class="line-2">SOCCER ACADEMY</span></p>
  </div>

  <div class="field-band">Field: Brookvale Turf&nbsp; 5 (1746 Hollowmere Lane Dunstead, MD 20419)</div>

  <section class="info-column info-column--time">
    <div class="column-head">TIME</div>
    <ul class="schedule">
      <li class="schedule-row"><span class="schedule-time">5:30pm-6:30pm</span><span class="schedule-age">5-8 years old</span></li>
      <li class="schedule-row"><span class="schedule-time">6;30pm-7:30pm</span><span class="schedule-age">9-12 years old</span></li>
      <li class="schedule-row"><span class="schedule-time">7:30pm-8:30pm</span><span class="schedule-age">13-18 years old</span></li>
    </ul>
  </section>

  <section class="info-column info-column--price">
    <div class="column-head column-head--orange">REGISTRATION</div>
    <div class="price">
      <p class="price-amount">$210</p>
      <p class="price-note">( Includes 1st month,<br>registration, practice uniform)</p>
    </div>
  </section>

  <section class="info-column info-column--online">
    <div class="column-head">REGISTER ONLINE</div>
    <div class="contact">
      <p class="contact-web">www.<span class="domain">valmoraacademy</span>.example</p>
      <p class="contact-phone">(240)555-0187</p>
    </div>
  </section>
</main>
</body>
</html>
```